Poster

I need a poster for my business, www.coastaltablejourneysbay.example which some information about the most important activities (Sangria Tasting, Iberian Ham, Charcuteries & Sherry Wine Tasting, Sailboat Experiences and Picnic Experiences). A3 Format. Social media included (@coastaltablejourneyctj), contact information included.

```html
<!DOCTYPE html>
<html lang="en">
<head>
<meta charset="utf-8">
<title>Coastal Table Journeys – Poster</title>
<link rel="stylesheet" href="https://fonts.googleapis.com/css2?family=Bebas+Neue&family=Montserrat:wght@700&display=swap">
<style>
  :root {
    --amber: #f0a019;
    --charcoal: #4a4645;
    --ink: #3b3939;
    --label: #555352;
    --white: #ffffff;
    --sky-top: #cfe3f0;
    --sea: #9fc0cf;
    --deck: #e4e1dc;
  }
  html, body { margin: 0; padding: 0; overflow: hidden; background: var(--amber); }
  .poster {
    position: relative; width: 850px; height: 1200px; overflow: hidden;
    background: var(--amber); font-family: "Montserrat", sans-serif;
  }
  .hero { position: absolute; left: 0; top: 0; width: 850px; height: 1000px; }
  .brand { position: absolute; left: 200px; top: 262px; display: flex; align-items: flex-start; gap: 28px; }
  .brand-mark { width: 54px; height: 54px; background: var(--amber); margin-top: 10px; }
  .brand-name {
    margin: 0; font-family: "Bebas Neue", sans-serif; font-weight: 400;
    font-size: 76px; line-height: 0.92; color: var(--ink); letter-spacing: 1px;
  }
  .activity { position: absolute; width: 170px; text-align: center; transform: translateX(-50%); }
  .activity-photo {
    position: absolute; width: 160px; height: 160px; border-radius: 50%;
    border: 3px solid var(--amber); box-sizing: border-box; transform: translate(-50%, -50%);
  }
  .activity-label {
    margin: 0; font-weight: 700; font-size: 20px; line-height: 1.2; color: var(--label);
  }
  .services {
    position: absolute; top: 1022px; left: 0; width: 850px; display: flex; justify-content: center; gap: 80px;
    font-family: "Bebas Neue", sans-serif; font-size: 42px; color: var(--white); letter-spacing: 0.5px;
  }
  .contact {
    position: absolute; left: 0; top: 1103px; width: 850px; height: 97px; background: var(--charcoal);
    display: grid; grid-template-columns: 330px 1fr; grid-template-rows: 34px 34px; row-gap: 0;
    padding: 16px 0 0 52px; box-sizing: border-box;
  }
  .contact-item { display: flex; align-items: center; gap: 14px; color: var(--white); font-weight: 700; font-size: 16.5px; }
  .contact-item svg { width: 24px; height: 24px; flex: none; }
</style>
</head>
<body>
<div class="poster">
  <svg class="hero" viewBox="0 0 850 1000" aria-hidden="false">
    <defs>
      <linearGradient id="seaSky" x1="0" y1="0" x2="0" y2="1">
        <stop offset="0" stop-color="#c5dcec"/>
        <stop offset="0.35" stop-color="#e6eff4"/>
        <stop offset="0.45" stop-color="#b7d0da"/>
        <stop offset="0.7" stop-color="#c9d8dc"/>
        <stop offset="1" stop-color="#e7e4df"/>
      </linearGradient>
    </defs>
    <path d="M600 960 C700 955 790 940 831 925 L831 950 C760 975 680 985 600 980 Z" fill="var(--charcoal)"/>
    <path role="img" aria-label="Photo of a sailboat deck heading out to sea under a bright sky"
          d="M19 19 H831 V935 C700 985 560 985 425 978 C260 970 120 945 19 920 Z" fill="url(#seaSky)"/>
  </svg>

  <div class="brand">
    <div class="brand-mark"></div>
    <h1 class="brand-name">Coastal<br>Table<br>Journeys</h1>
  </div>

  <div class="activity-photo" style="left:150px;top:688px;background:radial-gradient(circle at 55% 60%,#8a2b2b,#6e5a4d 55%,#a39383);" role="img" aria-label="Glass of sangria with orange slice"></div>
  <div class="activity-photo" style="left:332px;top:714px;background:radial-gradient(circle at 50% 60%,#b8464f,#b58a5e 55%,#9fb8c4);" role="img" aria-label="Board of sliced Iberian ham"></div>
  <div class="activity-photo" style="left:517px;top:709px;background:radial-gradient(circle at 50% 50%,#c9a46a,#8a5a3c 60%,#4a3a2e);" role="img" aria-label="Charcuterie board with cheeses and olives"></div>
  <div class="activity-photo" style="left:700px;top:682px;background:linear-gradient(180deg,#6a4a3a,#b07a4a 45%,#e3c15a 75%,#7a5a3a);" role="img" aria-label="Sherry wine glasses with cheese"></div>

  <div class="activity" style="left:150px;top:796px;"><p class="activity-label">Sangria Tasting</p></div>
  <div class="activity" style="left:332px;top:828px;"><p class="activity-label">Iberian Ham</p></div>
  <div class="activity" style="left:517px;top:834px;"><p class="activity-label">Charcuteries</p></div>
  <div class="activity" style="left:697px;top:779px;"><p class="activity-label">Sherry Wine<br>&nbsp;&nbsp;Tasting</p></div>

  <div class="services">
    <span>• Sailboat Experiences</span>
    <span>• Picnic Experiences</span>
  </div>

  <div class="contact">
    <div class="contact-item">
      <svg viewBox="0 0 24 24"><path fill="var(--amber)" d="M6.6 2.5l3 3.2-2 2.6c1.3 3 3.6 5.4 6.6 6.8l2.6-2 3.2 3-2.2 3.4C10 18.8 4.8 13.6 3.2 4.7z"/></svg>
      +34 600 12 34 56
    </div>
    <div class="contact-item">
      <svg viewBox="0 0 24 24"><rect x="3" y="2" width="18" height="20" fill="none" stroke="var(--amber)" stroke-width="2"/><path fill="var(--amber)" d="M3 8h18v2H3z"/><path d="M3 2l9 7 9-7" fill="none" stroke="var(--amber)" stroke-width="0"/><path d="M2 5l10 7 10-7" fill="none" stroke="var(--amber)" stroke-width="2" transform="translate(0,-1)"/></svg>
      info@coastaltablejourneysbay.example
    </div>
    <div class="contact-item">
      <svg viewBox="0 0 24 24"><circle cx="12" cy="7" r="5" fill="var(--amber)"/><path fill="var(--amber)" d="M3 23v-4c0-4 4-6 9-6s9 2 9 6v4z"/></svg>
      @coastaltablejourneyctj
    </div>
    <div class="contact-item">
      <svg viewBox="0 0 24 24"><circle cx="12" cy="12" r="10" fill="none" stroke="var(--amber)" stroke-width="2"/><ellipse cx="12" cy="12" rx="4" ry="10" fill="none" stroke="var(--amber)" stroke-width="2"/><path d="M2 12h20" stroke="var(--amber)" stroke-width="2"/></svg>
      www.coastaltablejourneysbay.example
    </div>
  </div>
</div>
</body>
</html>
```